Modern Minimal Acne Clearing Set Retail Box

We need a design for our slide out packaging box. The packaging is for our Acne Clearing Set, which includes a cleanser and a cream. We would love something that's original,minimal and modern and not gender specific. Feel free to use your own take on design. Surprise us. I've attached dimensions of the box as well as some refrence images of some boxes we like. It doesn't have to be exactly like these images but its a good starting point. Ive also attached our logo (you can change the logo style if needed to fit your design), your free to use other fonts and colors to match your design. The back of the box will have the drug fact for both products.

Target Market(s)

Everybody

Industry/Entity Type

Beauty

Font styles to use
Sans Serif

Colors
3176b5
33a6d7
85cae6
33b8a4
86cfc6
1b1b1b
ececec

Requirements
Must have
• Originality

```html
<!DOCTYPE html>
<html lang="en">
<head>
<meta charset="utf-8">
<title>Acne Clearing Set – Front Panel</title>
<link rel="stylesheet" href="https://fonts.googleapis.com/css2?family=Tinos&display=swap">
<style>
  :root {
    --backdrop: #d3e2ea;
    --panel: #f7f7f7;
    --panel-edge: #e4e4e4;
    --tab-blue: #5ec3e6;
    --rule-blue: #33a6d7;
    --brand-ink: #4a2c2e;
    --text-ink: #1b1b1b;
    --art-tone: #ececec;
  }
  html, body {
    margin: 0;
    width: 1200px;
    height: 1200px;
    overflow: hidden;
    background: var(--backdrop);
  }
  .canvas {
    position: relative;
    width: 1200px;
    height: 1200px;
  }
  .front-panel {
    position: absolute;
    left: 340px;
    top: 80px;
    width: 520px;
    height: 1040px;
    background: var(--panel);
    border: 1px solid var(--panel-edge);
    box-sizing: border-box;
    overflow: hidden;
  }
  .pull-tab {
    position: absolute;
    left: 50%;
    top: -1px;
    transform: translateX(-50%);
    width: 136px;
    height: 68px;
    background: var(--tab-blue);
    border-radius: 0 0 68px 68px;
  }
  .brand-name {
    position: absolute;
    left: 0;
    right: 0;
    top: 430px;
    margin: 0;
    text-align: center;
    font-family: "Tinos", serif;
    font-weight: 400;
    font-size: 46px;
    letter-spacing: 1px;
    color: var(--brand-ink);
  }
  .title-rule {
    position: absolute;
    left: 50%;
    top: 532px;
    width: 100px;
    height: 3px;
    transform: translateX(-50%);
    background: var(--rule-blue);
  }
  .product-title {
    position: absolute;
    left: 0;
    right: 0;
    top: 560px;
    margin: 0;
    text-align: center;
    font-family: "Tinos", serif;
    font-weight: 400;
    font-size: 34px;
    color: var(--text-ink);
  }
  .product-art {
    position: absolute;
    left: 50%;
    bottom: 0;
    width: 150px;
    height: 340px;
    transform: translateX(-50%);
    background: linear-gradient(180deg, #f1f1f1 0%, var(--art-tone) 100%);
  }
</style>
</head>
<body>
  <main class="canvas">
    <section class="front-panel">
      <div class="pull-tab"></div>
      <h1 class="brand-name">Lunara MD</h1>
      <div class="title-rule"></div>
      <h2 class="product-title">Acne Clearing Set</h2>
      <div class="product-art" role="img" aria-label="Faint line drawing of a pump bottle and tube rising from the bottom edge"></div>
    </section>
  </main>
</body>
</html>
```